Community Management Company in need of WordPress templates for website redesign

We are a community association management company providing services to homeowner associations (HOAs), condominium associations, cooperatives, municipal utility districts, luxury high-rises and large master-planned communities within the Real Estate category.

We are looking to do a refresh of our site with newly-designed pages that are compatible with WordPress and can be uploaded to a domain with little complications.

We are interested in first having a landing page designed based on a specific audience and call to actions as described in the design brief file attached to this design project and pasted below:
Design Brief for TerraHolm Website Refresh

General Details:
Company Name: TerraHolm
Business Location: Carrollton, TX – HQ
Current website: www.terraholm-example.com

Overview:

We are looking to for a refresh of our site with newly-designed pages that are compatible with WordPress and can be uploaded to a domain with little complications.

Our target audience / target market:
HOA and Association Board Members, Real Estate Builders & Developers, Residents and Homeowners, Vendors, Potential Business Partners

Project scope:
Create a landing page template with the target audience of HOA Board Members who are prospects of TerraHolm
The goal of the landing page is to have them fill out the proposal form by having the page take them from our “why” message to our “how” and “what” messages so they are compelled to fill out the form. The new landing page needs to drive that behavior.
Our messages will include the following

Why messages:
• Because you deserve an exceptional community
• Because you and your residents deserve an exceptional lifestyle
• Because your community matters
• Because your residents matter
• Exceptional Community. Managed
• Exceptional Lifestyle. Delivered
How/What messages:

With over 25 years of experience, TerraHolm provides exceptional community management solutions with the transparency and visibility your community deserves. Our fully integrated services are provided at competitive prices with the best people, best practices, and best cloud-based and mobile app technology.

Our team is made up of the industry’s leading experts equipped to answer your questions quickly. Our team includes: certified managers, degreed and certified accountants, experienced, multi-lingual customer service representatives, technology staff and industry executives. We perform industry leading best practices, on behalf of the communities we serve, ensuring you receive the highest level support, guidance and tools to assist in performing your fiduciary duties. With our proprietary, cloud-based and mobile app technology, pertinent community information is at your fingertips. You will be empowered to manage the business affairs of your community anytime, from any device, anywhere.

Our community management services include personalized onsite management, portfolio management, full-service community maintenance services, community management for builders and property developers, and Virtual CAM (Community Association Manager) management.

Our community communication services include cloud-based board, resident, closing, and attorney portals and mobile app technology, providing the transparency and visibility into the business affairs that your community deserves. In addition, we provide several communication tools to keep homeowners and residents informed via our community website, newsletter and event services.

TerraHolm, one of the largest and fastest growing community management companies, is proud to provide exceptional services to hundreds of community associations from under 50 units to over 7,000 units in Arizona, California, Colorado, Florida, Georgia, Louisiana, Nevada, North Carolina, Oregon, Texas and Washington, including homeowner associations (HOAs), condominium associations, cooperatives, luxury high-rises, municipal utility districts and large master-planned communities.

Other page elements: additional content block/placeholders for:
• Link to Service description and technology pages
• Link to Mobile Apps page
• Request a proposal form fill content block
• Find an office form fill content block and link to local page upon completion of search via zip or state
• Contact us content block with information to include phone, email, fax, etc. and link to contact us landing page

Template Elements:
Files will also be uploaded including:
• Logo
• Colors
• Sales PPT for their reference

Please see attached design brief (file #4), logos (file #2&3), colors & branding standards (file #5) and a sales PPT deck (file #1) geared towards the audience for your reference.
Updates

Project Deadline Extended
Reason: I am extending the deadline by one week to give everyone a chance to provide updates based on the feedback and submissions. Thank you for all of your efforts. I look forward to seeing all of your designs.

Project Deadline Extended
Reason: Good day everyone, We are extending our deadline by one more week; so please continue to submit your designs and revisions. We look forward to seeing your work. Regards.

Thank you for all of your submissions.  I am in the process of getting votes tallied and should have some further information Tuesday of next week.

I am currently reviewing the votes and comments from the poll and will provide feedback within the next day; so please stay tuned.

We are conducting one more round of voting for the website refresh.  Once this is complete we will contact the finalists and make a selection shortly thereafter.  Thank you again for your participation.  Please stay tuned.

We are finalizing our 2nd poll and will request revisions, if appropriate.  Thank you.

Target Market(s)

HOA Board members per the design brief

Industry/Entity Type

Communication

Requirements
Must have
• focus on a landing page first; not the homepage design
Nice to have
• Please see design brief - File #4
Should not have
• home page elements for the time being.

```html
<!DOCTYPE html>
<html lang="en">
<head>
<meta charset="utf-8">
<title>TerraHolm – Exceptional Community Management</title>
<link rel="stylesheet" href="https://fonts.googleapis.com/css2?family=Ubuntu:wght@400;500;700&family=Noto+Serif:ital@1&display=swap">
<style>
  :root {
    --teal: #0f6a80;
    --teal-dark: #0c5a6d;
    --green: #4a7a2c;
    --green-dark: #0f4a12;
    --text: #3d3d3d;
    --muted: #8a8a8a;
    --panel: #f5f5f5;
    --line: #dedede;
    --white: #ffffff;
  }
  * { box-sizing: border-box; margin: 0; padding: 0; }
  html, body { width: 796px; height: 1200px; overflow: hidden; }
  body { position: relative; background: var(--white); font-family: "Ubuntu", sans-serif; color: var(--text); }

  .hero { position: absolute; left: 0; top: 0; width: 796px; height: 460px; }
  .hero-photo { position: absolute; inset: 0;
    background: radial-gradient(ellipse at 62% 38%, #f1d9c6 0%, #f3e6dc 28%, #f7f3f0 55%, #fbfbfb 80%); }
  .hero-wave { position: absolute; left: 0; top: 430px; width: 796px; height: 125px; }

  .brand { position: absolute; left: 96px; top: 26px; display: flex; align-items: center; gap: 8px; }
  .brand-mark { width: 22px; height: 22px; background: var(--teal); }
  .brand-name { font-size: 32px; font-weight: 700; color: var(--green); }
  .brand-sub { position: absolute; left: 136px; top: 64px; font-size: 8px; color: var(--teal-dark); letter-spacing: .5px; }

  .office-finder { position: absolute; left: 96px; top: 342px; width: 221px; height: 114px;
    background: var(--white); box-shadow: 0 1px 4px rgba(0,0,0,.2); border-radius: 3px; }
  .office-finder .head { position: relative; background: var(--green); color: var(--white);
    height: 66px; padding: 9px 10px; border-radius: 3px 3px 0 0; }
  .office-finder .head::after { content: ""; position: absolute; left: 18px; bottom: -8px;
    border: 8px solid transparent; border-bottom: 0; border-top-color: var(--green); }
  .office-finder h2 { font-size: 13.5px; font-weight: 500; letter-spacing: .2px; }
  .office-finder p { font-size: 9.5px; line-height: 12px; margin-top: 5px; color: #e4efdc; }
  .office-finder .row { display: flex; gap: 6px; padding: 15px 12px 0 12px; }
  .zip { flex: 1; height: 26px; border: 1px solid var(--line); font-size: 9.5px; color: var(--muted); padding: 7px 8px; }
  .btn { background: var(--green-dark); color: var(--white); font-size: 10.5px; font-weight: 500;
    display: flex; align-items: center; justify-content: center; border-radius: 2px; }
  .office-finder .btn { width: 65px; height: 26px; }

  .why { position: absolute; left: 0; top: 470px; width: 796px; height: 81px; color: var(--white); }
  .why-lead { position: absolute; left: 92px; top: 12px; }
  .why-lead .small { font-family: "Noto Serif", serif; font-style: italic; font-size: 17.5px; }
  .why-lead .big { font-size: 19px; font-weight: 500; letter-spacing: .4px; margin-top: 1px; }
  .why-list { position: absolute; top: 10px; list-style: none; font-size: 10.5px; line-height: 20px; }
  .why-list li::before { content: "-"; margin-right: 8px; }
  .why-list.a { left: 358px; }
  .why-list.b { left: 540px; top: 30px; }

  .story { position: absolute; left: 92px; top: 566px; width: 616px; font-size: 9.4px; line-height: 14.4px; }
  .story p + p { margin-top: 14.4px; }

  .contact-band { position: absolute; left: 0; top: 894px; width: 796px; height: 276px; background: var(--panel); }
  .proposal-form { position: absolute; left: 92px; top: 32px; width: 276px; }
  .field { background: var(--white); border: 1px solid var(--line); height: 30px; margin-bottom: 5px;
    font-size: 9px; color: #aaa; padding: 10px 10px; letter-spacing: .4px; }
  .field.message { height: 82px; }
  .proposal-form .btn { position: absolute; right: 0; top: 224px; width: 65px; height: 21px; }

  .contact-info { position: absolute; left: 397px; top: 32px; width: 320px; }
  .contact-info h3 { font-family: "Noto Serif", serif; font-style: italic; font-weight: 400; font-size: 12.5px; color: #555; }
  .contact-info .hours { font-size: 9.3px; color: var(--muted); margin-top: 12px; }
  .contact-info dl { margin-top: 12px; display: grid; grid-template-columns: 46px auto; row-gap: 5px; font-size: 9.3px; }
  .contact-info dt { font-weight: 500; color: #555; }
  .contact-info dd { color: var(--muted); }
  .social { display: flex; gap: 5px; margin-top: 18px; }
  .social span { width: 18px; height: 18px; background: #444; border-radius: 2px; }
  .app-badge { width: 92px; height: 31px; background: #111; border-radius: 4px; margin-top: 22px; }

  .site-footer { position: absolute; left: 0; top: 1170px; width: 796px; height: 30px; background: var(--teal);
    color: var(--white); font-size: 8.5px; }
  .site-footer .copy { position: absolute; left: 92px; top: 11px; }
  .site-footer nav { position: absolute; right: 92px; top: 10px; display: flex; gap: 14px; }
</style>
</head>
<body>
  <header class="hero">
    <div class="hero-photo" role="img" aria-label="Photograph of a smiling family of four relaxing together on a white bed"></div>
    <svg class="hero-wave" viewBox="0 0 796 125" preserveAspectRatio="none" aria-hidden="true">
      <path d="M0 28 C 220 48, 520 -10, 796 18 L796 125 L0 125 Z" fill="var(--teal)"/>
    </svg>
    <div class="brand"><span class="brand-mark"></span><span class="brand-name">TerraHolm</span></div>
    <div class="brand-sub">POWERED BY LINQBASE</div>

    <form class="office-finder">
      <div class="head">
        <h2>FIND A TERRAHOLM OFFICE</h2>
        <p>Find a TerraHolm office nearest you by entering your zip code</p>
      </div>
      <div class="row"><div class="zip">Zip Code</div><div class="btn">SUBMIT</div></div>
    </form>
  </header>

  <section class="why">
    <div class="why-lead">
      <div class="small">Because you deserve an</div>
      <div class="big">EXCEPTIONAL COMMUNITY</div>
    </div>
    <ul class="why-list a">
      <li>Because you and your residents deserve an exceptional lifestyle</li>
      <li>Because your residents matter</li>
      <li>Exceptional Lifestyle.&nbsp; Delivered</li>
    </ul>
    <ul class="why-list b">
      <li>Because your community matters</li>
      <li>Exceptional Community.&nbsp; Managed</li>
    </ul>
  </section>

  <main class="story">
    <p>With over 25 years of experience, TerraHolm provides exceptional community management solutions with the transparency and visibility your community deserves. Our fully integrated services are provided at competitive prices with the best people, best practices, and best cloud-based and mobile app technology.</p>
    <p>Our team is made up of the industry’s leading experts equipped to answer your questions quickly. Our team includes: certified managers, degreed and certified accountants, experienced, multi-lingual customer service representatives, technology staff and industry executives. We perform industry leading best practices, on behalf of the communities we serve, ensuring you receive the highest level support, guidance and tools to assist in performing your fiduciary duties. With our proprietary, cloud-based and mobile app technology, pertinent community information is at your fingertips. You will be empowered to manage the business affairs of your community anytime, from any device, anywhere.</p>
    <p>Our community management services include personalized onsite management, portfolio management, full-service community maintenance services, community management for builders and property developers, and Virtual CAM (Community Association Manager) management.</p>
    <p>Our community communication services include cloud-based board, resident, closing, and attorney portals and mobile app technology, providing the transparency and visibility into the business affairs that your community deserves. In addition, we provide several communication tools to keep homeowners and residents informed via our community website, newsletter and event services.</p>
    <p>TerraHolm, one of the largest and fastest growing community management companies, is proud to provide exceptional services to hundreds of community associations from under 50 units to over 7,000 units in Arizona, California, Colorado, Florida, Georgia, Louisiana, Nevada, North Carolina, Oregon, Texas and Washington, including homeowner associations (HOAs), condominium associations, cooperatives, luxury high-rises, municipal utility districts and large master-planned communities.</p>
  </main>

  <section class="contact-band">
    <form class="proposal-form">
      <div class="field">NAME</div>
      <div class="field">EMAIL ADDRESS</div>
      <div class="field">SUBJECT</div>
      <div class="field message">MESSAGE</div>
      <div class="btn">SUBMIT</div>
    </form>
    <div class="contact-info">
      <h3>Contact Info</h3>
      <p class="hours">We are open from 7:30 a.m. - 7:00 p.m. Central time, Monday through Friday.</p>
      <dl>
        <dt>PHONE:</dt><dd>800-555-0142&nbsp; (800-555-0143)</dd>
        <dt>FAX:</dt><dd>800-555-0187</dd>
        <dt>EMAIL:</dt><dd>SERVICE@TERRAHOLM-EXAMPLE.COM</dd>
      </dl>
      <div class="social" aria-label="Social links"><span></span><span></span><span></span><span></span><span></span><span></span></div>
      <div class="app-badge" aria-label="App download badge"></div>
    </div>
  </section>

  <footer class="site-footer">
    <div class="copy">© 2014 TerraHolm LLC. All rights reserved.</div>
    <nav><span>Home</span><span>About Us</span><span>Services</span><span>Mobile Apps</span><span>Contact Us</span></nav>
  </footer>
</body>
</html>
```